New Dynamic Design Based on Other Site

We need a new website designed where the front page is VERY SEO Friendly. The front page should almost follow the same SEO principles that are on BrixelLayout.com. The inner pages need to follow the same exact video animations that occur on quolm.com. I'd like to keep our "marlowes" theme throughout the new design but we will provide all of the content but I want someone to design something SEO friendly, new blog theme, and actual inner pages that are dynamic and based on those short videos.

Check attached file for company name and site that we currently have. Feel free to pull the content from that site and re-use it and also leave placeholders for the rest of them.

PLEASE NO USE OF STOCK IMAGES. Use a designer or an illustrator to create the various images.
Updates

Please make sure the front page is SEO friendly! Make sure you familiarize yourself with the vantro algorithm for SEO. Content above the fold H1 Tags Very mobile friendly Minimal javascript and animations Basically a quality static page with optimized content

Reason: Still waiting on some more designs.

Target Market(s)

call center companies, anything call related

Industry/Entity Type

Telecommunications

Number of Pages Required

4 page

Font styles to use
Sans Serif

Colors
33a6d7
85cae6
0792cd
0255a3
cee9f5
ecf7fb
ffffff

Requirements
Must have
• places for video animations
• dynamic functionality
• SEO friendly (front page)
Should not have
• should not look like a template. needs to be unique

```html
<!DOCTYPE html>
<html lang="en">
<head>
<meta charset="utf-8">
<title>Dial Meridian — Call Center Consulting</title>
<link rel="stylesheet" href="https://fonts.googleapis.com/css2?family=Roboto:wght@300;400;500;700&display=swap">
<style>
:root{
  --sky:#33a6d7;
  --sky-light:#85cae6;
  --blue:#0792cd;
  --navy:#0255a3;
  --ice:#cee9f5;
  --mist:#ecf7fb;
  --white:#ffffff;
  --ink:#1b1f24;
  --grey-text:#7a808a;
  --panel:#f1f4f7;
  --backdrop:#222325;
  --footer:#141516;
}
*{box-sizing:border-box;margin:0;padding:0}
html,body{width:1200px;height:2380px;overflow:hidden}
body{background:var(--backdrop);font-family:'Roboto',Arial,sans-serif;color:var(--ink)}
h1,h2,h3,h4{font-weight:400}
.page{position:absolute;left:232px;top:28px;width:768px;height:2322px;background:var(--white);overflow:hidden}
.abs{position:absolute}

/* header */
.site-header{left:0;top:0;width:768px;height:55px}
.header-bar{left:0;top:0;width:531px;height:55px;background:linear-gradient(90deg,var(--navy),var(--blue))}
.brand{left:46px;top:18px;display:flex;align-items:center;gap:6px;color:var(--white);font-weight:500;font-size:15px}
.brand-dot{width:16px;height:16px;border-radius:50%;background:var(--sky-light)}
.main-nav{left:282px;top:24px;display:flex;gap:14px;font-size:8px;font-weight:500;color:var(--white);letter-spacing:.2px}
.header-tools{left:540px;top:23px;display:flex;gap:12px;font-size:8px;color:var(--ink);align-items:center}
.tool-dot{width:6px;height:6px;border-radius:50%;background:var(--navy)}

/* hero */
.hero{left:0;top:55px;width:768px;height:273px;background:linear-gradient(100deg,var(--mist) 0%,var(--ice) 45%,var(--sky-light) 100%)}
.hero-title{left:46px;top:28px;font-size:13px;font-weight:700;letter-spacing:2.4px;color:var(--navy);line-height:29px}
.hero-lead{left:46px;top:120px;width:330px;font-size:13px;line-height:20px;color:var(--navy)}
.btn{display:inline-block;background:var(--navy);color:var(--white);font-size:7px;font-weight:700;letter-spacing:.5px;text-align:center}
.hero-btn{left:46px;top:212px;width:104px;height:26px;line-height:26px}
.hero-band{left:0;top:328px;width:768px;height:40px;background:linear-gradient(90deg,var(--navy),var(--blue))}
.slider-dots{left:310px;top:0;height:40px;display:flex;gap:8px;align-items:center}
.slider-dots .dot{width:5px;height:5px;border-radius:50%;background:var(--sky-light)}
.slider-dots .on{width:10px;height:10px;background:var(--white)}
.slider-dots .ring{width:9px;height:9px;border-radius:50%;border:1px solid var(--sky-light)}
.slider-dots .arrow{color:var(--sky-light);font-size:12px;line-height:1;margin:0 12px}

/* about */
.eyebrow{font-size:9px;font-weight:700;letter-spacing:1.3px;color:var(--navy)}
.about-eyebrow{left:46px;top:400px}
.about-heading{left:46px;top:440px;width:260px;font-size:19px;line-height:25px}
.small-copy{font-size:8px;line-height:13px;color:var(--grey-text)}
.about-copy{left:297px;top:438px;width:426px}
.read-more{left:656px;top:500px;font-size:8px;color:var(--blue)}
.photo-call{left:297px;top:546px;width:426px;height:244px;background:linear-gradient(120deg,#8b9a83,#c7d0c6 55%,#6a7568)}
.quote-box{left:47px;top:610px;width:369px;height:218px;background:linear-gradient(135deg,var(--navy),var(--blue))}
.quote-text{left:42px;top:44px;width:300px;font-size:18px;line-height:24px;color:var(--white);font-weight:400}
.quote-rule{left:42px;top:170px;width:55px;height:3px;background:var(--sky-light)}

/* profile */
.profile-panel{left:0;top:828px;width:483px;height:272px;background:var(--panel)}
.profile-eyebrow{left:99px;top:22px}
.profile-heading{left:99px;top:44px;font-size:17px}
.profile-copy{left:99px;top:76px;width:330px}
.profile-btn{left:99px;top:214px;width:83px;height:27px;line-height:27px}
.photo-desk{left:458px;top:876px;width:265px;height:181px;background:linear-gradient(120deg,#e8ecef,#c9d2d8 60%,#8f9aa3)}

/* testimonials */
.testimonials{left:0;top:1101px;width:768px;height:273px;background:linear-gradient(180deg,#4f88b8 0%,#2d6aa3 50%,#1d4f86 100%)}
.testimonials-title{left:46px;top:98px;font-size:20px;line-height:24px;color:var(--white)}
.testimonial-quote{left:330px;top:82px;width:380px;text-align:center;font-size:14px;line-height:20px;color:var(--white)}
.testimonial-name{left:330px;top:146px;width:380px;text-align:center;font-size:12px;font-weight:700;color:var(--white)}
.testimonial-dots{left:505px;top:198px;display:flex;gap:4px}
.testimonial-dots span{width:5px;height:5px;border-radius:50%;background:var(--ice)}

/* services */
.services-eyebrow{left:46px;top:1408px}
.services-heading{left:46px;top:1436px;width:410px;font-size:19px;line-height:25px}
.video-slot{left:475px;top:1402px;width:248px;height:123px;background:linear-gradient(120deg,#2c2e33,#6b6f76 55%,#2a2c30)}
.play{left:108px;top:46px}
.service-card{top:1546px;width:153px;height:155px;background:var(--mist);text-align:center}
.service-card.active{background:linear-gradient(135deg,var(--navy),var(--blue));color:var(--white)}
.service-card svg{margin-top:48px}
.service-name{margin-top:14px;font-size:8px;font-weight:500;line-height:11px;letter-spacing:.3px}

/* pricing */
.pricing-heading{left:47px;top:1742px;font-size:19px}
.price-card{top:1794px;width:210px;height:249px}
.coaching{left:47px;background:linear-gradient(135deg,var(--navy),var(--blue));color:var(--white);padding:22px 18px}
.coaching h3{font-size:20px}
.coaching .tag{margin-top:18px;font-size:9px;font-weight:500}
.coaching .amount{margin-top:16px;font-size:20px}
.coaching .note{margin-top:12px;font-size:9px;line-height:12px;font-weight:500}
.outline-btn{margin-top:16px;display:inline-block;border:1px solid var(--white);font-size:9px;padding:6px 14px}
.plan{background:var(--mist)}
.plan-photo{width:100%;height:122px;background:linear-gradient(120deg,#8c9aa5,#d9dfe3 55%,#6f7c86)}
.plan-tag{left:14px;top:10px;background:var(--blue);color:var(--white);font-size:9px;padding:4px 12px}
.plan-text{left:18px;top:138px;width:180px;font-size:9px;line-height:12px}
.plan-price{left:18px;top:198px;font-size:18px}
.pricing-btn{left:341px;top:2067px;width:84px;height:29px;line-height:29px}

/* footer */
.site-footer{left:0;top:2122px;width:768px;height:200px;background:var(--footer);color:#b9bdc2}
.footer-brand{left:46px;top:70px;display:flex;align-items:center;gap:6px;font-size:19px;color:var(--sky)}
.footer-brand .brand-dot{width:22px;height:22px;background:var(--sky)}
.copyright{left:46px;top:166px;font-size:7px;color:#8d9197}
.footer-col h4{font-size:13px;color:#d4d7db;margin-bottom:10px}
.footer-col ul{list-style:none;font-size:8px;line-height:15px}
.footer-col li::before{content:"•";margin-right:6px;color:#6b6f75}
.quick{left:243px;top:18px}
.contact{left:385px;top:18px}
.contact p{font-size:8px;line-height:13px}
.social{left:541px;top:30px;display:flex;gap:10px}
.social span{width:19px;height:19px;border-radius:50%;background:#3a3c40}
.subscribe{left:541px;top:76px;width:182px;height:24px;background:var(--white);color:#444;font-size:8px;padding:7px 8px}
.subscribe svg{position:absolute;right:7px;top:6px}
</style>
</head>
<body>
<main class="page">

  <header class="site-header abs">
    <div class="header-bar abs"></div>
    <div class="brand abs"><span class="brand-dot"></span>Dial Meridian</div>
    <nav class="main-nav abs"><span>ABOUT US</span><span>SERVICES ▾</span><span>SELF-FUNDING</span><span>CONTACT US</span></nav>
    <div class="header-tools abs">
      <span>☎ +1 555 014 22</span><span class="tool-dot"></span><span class="tool-dot"></span><span class="tool-dot"></span>
      <svg width="9" height="9" viewBox="0 0 10 10" style="margin-left:36px"><circle cx="4" cy="4" r="3" fill="none" stroke="#1b1f24" stroke-width="1.4"/><line x1="6.3" y1="6.3" x2="9" y2="9" stroke="#1b1f24" stroke-width="1.4"/></svg>
    </div>
  </header>

  <section class="hero abs" role="img" aria-label="Photo of a smiling call center agent wearing a headset">
    <h2 class="hero-title abs">LOREM IPSUM DUMMY<br>LOREM IPSUM<br>LOREM</h2>
    <p class="hero-lead abs">Lorem Ipsum is simply dummy text of the printing and typesetting industry.</p>
    <span class="btn hero-btn abs">KNOW MORE</span>
  </section>
  <div class="hero-band abs">
    <div class="slider-dots abs"><span class="arrow">‹</span><span class="dot"></span><span class="dot"></span><span class="dot on"></span><span class="ring"></span><span class="dot"></span><span class="arrow">›</span></div>
  </div>

  <section>
    <p class="eyebrow about-eyebrow abs">ABOUT DIAL MERIDIAN</p>
    <h1 class="about-heading abs">Lorem ipsum dummy text here.</h1>
    <p class="small-copy about-copy abs">Lorem Ipsum is simply dummy text of the printing and typesetting industry. Lorem Ipsum has been the industry's standard dummy text ever since the 1500s, when an unknown printer took a galley of type and scrambled it to make a type specimen book. Lorem Ipsum is simply dummy text of the printing and typesetting industry. Lorem Ipsum has been the industry's standard dummy.</p>
    <span class="read-more abs">Read More ⟶</span>
  </section>

  <div class="photo-call abs" role="img" aria-label="Photo of a businessman in a suit talking on a phone outdoors"></div>
  <div class="quote-box abs">
    <p class="quote-text abs">Lorem Ipsum is simply dummy text of the printing and typesetting industry. Lorem Ipsum has been the industry'</p>
    <span class="quote-rule abs"></span>
  </div>

  <section class="profile-panel abs">
    <p class="eyebrow profile-eyebrow abs">ABOUT SUCCESS</p>
    <h2 class="profile-heading abs">Company Profile</h2>
    <p class="small-copy profile-copy abs">Lorem Ipsum is simply dummy text of the printing and typesetting industry. Lorem Ipsum has been the industry's standard dummy text ever since the 1500s, when an unknown printer took a galley of type and scrambled it to make a type specimen book. Lorem Ipsum is simply dummy text of the printing and typesetting industry. Lorem Ipsum has been the industry's standard dummy text ever since the 1500s, when an unknown printer took a galley of type and scrambled it to make a type specimen book.</p>
    <span class="btn profile-btn abs">MORE INFO</span>
  </section>
  <div class="photo-desk abs" role="img" aria-label="Photo of a woman on the phone at a bright office desk"></div>

  <section class="testimonials abs" role="img" aria-label="Photo of a person standing on a mountain ridge under a blue sky">
    <h2 class="testimonials-title abs">Notable Comments<br>About Dial Meridian</h2>
    <p class="testimonial-quote abs">“Nunc maximus purus tincidunt, vestibulum elit posuere, accumsan ligula.”</p>
    <p class="testimonial-name abs">Mara Velden</p>
    <div class="testimonial-dots abs"><span></span><span></span><span></span></div>
  </section>

  <section>
    <p class="eyebrow services-eyebrow abs">CORE SERVICES</p>
    <h2 class="services-heading abs">Lorem Ipsum is simply dummy text of the printing and scrambled.</h2>
    <div class="video-slot abs" role="img" aria-label="Video still of a man speaking into a microphone">
      <svg class="play abs" width="34" height="34" viewBox="0 0 34 34"><circle cx="17" cy="17" r="15" fill="none" stroke="#fff" stroke-width="2"/><path d="M13 10 L24 17 L13 24 Z" fill="#fff"/></svg>
    </div>
    <div class="service-card active abs" style="left:47px">
      <svg width="30" height="30" viewBox="0 0 30 30" fill="none" stroke="#fff" stroke-width="1.4"><circle cx="17" cy="9" r="6"/><path d="M3 22 h6 l5 3 h9 l4-4"/><text x="14.5" y="12" font-size="8" fill="#fff" stroke="none">$</text></svg>
      <p class="service-name">COMPENSATION<br>CONSULTING</p>
    </div>
    <div class="service-card abs" style="left:221px">
      <svg width="30" height="30" viewBox="0 0 30 30" fill="none" stroke="#0255a3" stroke-width="1.4"><rect x="9" y="3" width="12" height="9"/><path d="M15 12 v5 M6 17 h18 M6 17 v4 M24 17 v4"/><circle cx="6" cy="24" r="3"/><circle cx="24" cy="24" r="3"/></svg>
      <p class="service-name">CORPORATE<br>ETHICS PROGRAM</p>
    </div>
    <div class="service-card abs" style="left:395px">
      <svg width="30" height="30" viewBox="0 0 30 30" fill="none" stroke="#0255a3" stroke-width="1.4"><circle cx="15" cy="10" r="7"/><path d="M15 17 v4 M6 21 h18 M6 21 v4 M15 21 v4 M24 21 v4"/></svg>
      <p class="service-name">LEADERSHIP<br>TRAINING</p>
    </div>
    <div class="service-card abs" style="left:569px">
      <svg width="30" height="30" viewBox="0 0 30 30" fill="none" stroke="#0255a3" stroke-width="1.4"><path d="M15 22 v-10 M15 14 c-6 0-8-4-8-8 c5 0 8 3 8 8 M15 12 c0-5 3-8 8-8 c0 5-3 8-8 8"/><path d="M3 24 h6 l5 3 h9 l4-4"/></svg>
      <p class="service-name">TALENT<br>ACQUISITION</p>
    </div>
  </section>

  <section>
    <h2 class="pricing-heading abs">Simple Pricing</h2>
    <div class="price-card coaching abs">
      <h3>Coaching</h3>
      <p class="tag">When you simply need the very best</p>
      <p class="amount">$7,000/Session</p>
      <p class="note">The most prestigious coaching focused on achieving your ultimate and highest level of potential</p>
      <span class="outline-btn">More Info</span>
    </div>
    <div class="price-card plan abs" style="left:279px">
      <div class="plan-photo" role="img" aria-label="Photo of two colleagues meeting at a table"></div>
      <span class="plan-tag abs">Small Groups</span>
      <p class="plan-text abs">Gain entry into the Best Accountability Group EVER</p>
      <p class="plan-price abs">$164.99/Month</p>
    </div>
    <div class="price-card plan abs" style="left:509px">
      <div class="plan-photo" role="img" aria-label="Photo of a group of professionals seated in a row"></div>
      <span class="plan-tag abs">PACE</span>
      <p class="plan-text abs">You Can't Tell Where You're Going If You Don't Know Where You've Been</p>
      <p class="plan-price abs">$59.99/Month</p>
    </div>
    <span class="btn pricing-btn abs">MORE INFO</span>
  </section>

  <footer class="site-footer abs">
    <div class="footer-brand abs"><span class="brand-dot"></span>Dial Meridian</div>
    <p class="copyright abs">©2017 Dial Meridian. All rights reserved</p>
    <div class="footer-col quick abs">
      <h4>Quick links</h4>
      <ul><li>Home</li><li>Recruiting Firms</li><li>Hiring Managers</li><li>PACE Mobile</li><li>Apex Plan</li><li>Small Groups</li><li>Library</li></ul>
    </div>
    <div class="footer-col contact abs">
      <h4>Contact Details</h4>
      <p>Harbor Suites<br>418 Larkspur Lane<br>Eastvale, Nevada 89000<br>P: 555 010 2468</p>
    </div>
    <div class="social abs"><span></span><span></span><span></span><span></span><span></span><span></span></div>
    <div class="subscribe abs">Subscribe: Enter your email address
      <svg width="10" height="10" viewBox="0 0 10 10"><path d="M0 5 L10 0 L7 10 L5 6 Z" fill="#141516"/></svg>
    </div>
  </footer>

</main>
</body>
</html>
```